Brackwater Vale Medical Website to make connecting and communicating easier

To create a unique, user-friendly, professional website for patients and professionals to access education/ information, forms, appointments, contact details, and data about us, and for us to have the capacity to link to various cloud-based platforms.
To use the logo design and colour scheme we have just sourced.

WEBSITE to be eye catching, Inspiring and alluring
- efficient and logical
- professional and trustworthy appearance
- health focus "living health matters"
- user friendly
- ability to link with cloud-based software and video conferencing tools/ telehealth
- colours- black/ white teal and ?silver

PAGES:
page 1 - Our clinic and staff, services offered, contact us- address/ map / contact details- social media connections
page 2- patients and visitors - New patient forms to complete, news and patient informtion (educatinal)
page 3 - health professionals -referral forms, research and education
page 3- online appointments
page 4 - Quick links - partners, other services
page 5- privacy policy, disclaimer

Need extra days to review

HI, Could we please extend the deadline another 5 days, so sorry just struggling with my workload to be able to keep up and I am wanting to liaise more with the designer that I will choose. I am so happy with PixelForge and all the designers - thank you! Thank you so much!!

Target Market(s)

Patients - mostly over 60's so the website must be minimal clicks and simple to navigate
Professionals - for education and access forms

Industry/Entity Type

Health Care

Coding

Coded - Design and coding required

Number of Pages Required

5+ page

Font styles to use
Sans Serif
Script

Colors
33b8a4
86cfc6

Requirements
Must have
• WEBSITE to be eye catching, Inspiring and alluring
- efficient and logical
- user friendly

WEBSITE - professional and user friendly
- ability to link with cloud based software and videoconferencing/ telehealth
Nice to have
• clean and crisp presentation
happy for an innovative look
room to add more services and ability to link pages and resources
Should not have
• Please ensure the website is not:
clunky
difficult to navigate
common and cheap looking

```html
<!DOCTYPE html>
<html lang="en">
<head>
<meta charset="utf-8">
<title>Brackwater Vale Medical — Living Health Matters</title>
<link href="https://fonts.googleapis.com/css2?family=Montserrat:wght@400;500;600;700&family=Open+Sans:wght@400;600&display=swap" rel="stylesheet">
<style>
:root{
  --teal:#33b8a4;
  --teal-soft:#86cfc6;
  --teal-deep:#2a9d8c;
  --ink:#1f1f1f;
  --panel:#262626;
  --text:#3a3a3a;
  --muted:#6b6b6b;
  --white:#ffffff;
  --silver:#e9eef0;
}
*{box-sizing:border-box;margin:0;padding:0}
html,body{width:1200px;height:5357px;overflow:hidden}
body{position:relative;background:var(--white);font-family:"Open Sans",Arial,sans-serif;color:var(--text)}
.abs{position:absolute}
.btn{position:absolute;background:var(--teal);color:var(--white);font-family:"Montserrat",sans-serif;font-weight:600;font-size:17px;letter-spacing:.5px;display:flex;align-items:center;justify-content:center;border-radius:4px;text-transform:uppercase}
.section-title{position:absolute;left:0;width:1200px;text-align:center;font-family:"Montserrat",sans-serif;font-weight:700;font-size:40px;color:var(--ink);letter-spacing:1px}
.section-title span{color:var(--teal);font-weight:500}
.lede{position:absolute;left:240px;width:720px;text-align:center;font-size:14px;line-height:19px;color:var(--text)}
.brand{font-family:"Montserrat",sans-serif;font-weight:700;color:var(--teal);display:flex;align-items:center;gap:10px}
.brand i{display:block;border-radius:50%;background:var(--teal)}

/* header */
.topbar{left:720px;top:20px;font-size:11px;color:var(--text);display:flex;align-items:center;gap:6px}
.social{display:flex;gap:6px}
.social b{display:block;width:16px;height:16px;border-radius:50%}
.navband{left:0;top:96px;width:1200px;height:41px;background:var(--teal)}
.navband .cta{position:absolute;right:0;top:0;width:196px;height:41px;background:var(--ink);color:var(--white);font-family:"Montserrat",sans-serif;font-size:12px;font-weight:600;display:flex;align-items:center;justify-content:center}
.nav{position:absolute;left:365px;top:0;height:41px;display:flex;gap:26px;align-items:center;color:var(--white);font-family:"Montserrat",sans-serif;font-size:14px;font-weight:500}
.header-brand{left:96px;top:36px;width:200px;height:100px;background:var(--white)}
.header-brand .brand{position:absolute;left:6px;top:22px;font-size:20px;line-height:24px;width:190px}

/* hero */
.hero-photo{left:0;top:146px;width:1200px;height:950px;background:
  radial-gradient(ellipse 420px 260px at 760px 560px,rgba(170,215,235,.85),rgba(170,215,235,0) 70%),
  radial-gradient(ellipse 380px 300px at 170px 820px,rgba(150,110,70,.85),rgba(150,110,70,0) 70%),
  radial-gradient(ellipse 300px 200px at 1080px 720px,rgba(190,200,150,.6),rgba(190,200,150,0) 70%),
  radial-gradient(ellipse 700px 200px at 600px 120px,rgba(255,255,255,.9),rgba(255,255,255,0) 70%),
  linear-gradient(180deg,#e6ecef 0%,#c9d6dd 40%,#b8c8d0 70%,#d7dcdc 100%)}
.hero-title{left:129px;top:395px;font-family:"Montserrat",sans-serif;font-weight:600;font-size:56px;color:var(--ink)}
.hero-sub{left:131px;top:468px;font-size:24px;line-height:35px;color:var(--ink);width:520px}

/* booking panel */
.book{left:607px;top:762px;width:458px;height:534px;background:var(--panel);color:var(--white)}
.book h3{position:absolute;left:0;width:100%;top:50px;text-align:center;font-family:"Montserrat",sans-serif;font-weight:600;font-size:31px}
.field{position:absolute;height:36px;border:1px solid #4a4a4a;background:#2c2c2c;color:var(--white);font-family:"Montserrat",sans-serif;font-size:12px;padding-left:16px;display:flex;align-items:center}
.drop{position:absolute;right:0;top:0;width:40px;height:34px;background:var(--teal)}

/* about */
.about-title{left:135px;top:1050px;font-family:"Montserrat",sans-serif;font-weight:700;font-size:42px;color:var(--ink);display:flex;align-items:flex-end;gap:16px}
.about-title .brand{font-size:16px;line-height:18px;width:170px;margin-bottom:6px}
.about-copy{left:135px;top:1107px;width:440px;font-size:14px;line-height:25px;color:var(--text)}

/* services */
.svc-card{position:absolute;top:1562px;width:326px;height:296px;border:4px solid var(--teal);background:
  radial-gradient(ellipse 120px 160px at 150px 130px,rgba(250,250,252,.95),rgba(250,250,252,0) 70%),
  radial-gradient(ellipse 110px 90px at 60px 250px,rgba(225,200,170,.9),rgba(225,200,170,0) 70%),
  radial-gradient(ellipse 90px 140px at 60px 90px,rgba(60,110,170,.7),rgba(60,110,170,0) 70%),
  radial-gradient(ellipse 100px 120px at 270px 200px,rgba(120,150,175,.8),rgba(120,150,175,0) 70%),
  linear-gradient(180deg,#c9d5de,#a8b8c4 60%,#d9dcdc)}
.svc-label{position:absolute;top:1884px;width:326px;text-align:center;font-family:"Montserrat",sans-serif;font-weight:600;font-size:19px;color:var(--ink)}
.arrow{position:absolute;top:1672px;font-size:44px;color:var(--ink);font-family:"Montserrat",sans-serif}

/* why */
.why-bg{left:0;top:1780px;width:1200px;height:1240px;background:linear-gradient(180deg,#e8f6f3 0%,#bfe3dd 30%,#8cc5bc 65%,#6aa59c 100%)}
.why-icon{position:absolute;top:2217px;width:134px;height:134px;border-radius:50%;background:var(--ink);border:5px solid #f0f0f0;box-shadow:0 0 0 2px var(--ink)}
.why-icon svg{position:absolute;left:30px;top:30px}
.why-title{position:absolute;top:2376px;width:260px;text-align:center;font-family:"Montserrat",sans-serif;font-weight:600;font-size:20px;color:var(--white);letter-spacing:.5px}
.why-copy{position:absolute;top:2410px;width:260px;text-align:center;font-size:14px;line-height:18px;color:var(--white)}
.mini{position:absolute;top:2494px;width:46px;height:46px;border-radius:50%;background:var(--teal);color:var(--white);display:flex;align-items:center;justify-content:center;font-size:22px}

/* offer */
.offer{position:absolute;top:2845px;width:468px;height:290px;border:4px solid #cfe8b8;overflow:hidden;background:
  radial-gradient(ellipse 120px 140px at 90px 110px,rgba(120,70,50,.75),rgba(120,70,50,0) 70%),
  radial-gradient(ellipse 140px 150px at 330px 110px,rgba(240,215,180,.95),rgba(240,215,180,0) 70%),
  radial-gradient(ellipse 150px 120px at 400px 230px,rgba(175,40,120,.75),rgba(175,40,120,0) 70%),
  radial-gradient(ellipse 120px 100px at 220px 200px,rgba(255,255,255,.9),rgba(255,255,255,0) 70%),
  linear-gradient(135deg,#e9ddd3,#f5ede6 50%,#e3c6d1)}
.offer.pro{background:
  radial-gradient(ellipse 180px 100px at 160px 80px,rgba(160,110,70,.7),rgba(160,110,70,0) 70%),
  radial-gradient(ellipse 140px 90px at 120px 70px,rgba(60,110,160,.55),rgba(60,110,160,0) 70%),
  radial-gradient(ellipse 110px 140px at 340px 100px,rgba(240,215,170,.9),rgba(240,215,170,0) 70%),
  radial-gradient(ellipse 150px 120px at 350px 250px,rgba(40,110,180,.9),rgba(40,110,180,0) 70%),
  linear-gradient(135deg,#e4e6e6,#f2f2ef 50%,#c8d6e2)}
.offer .cap{position:absolute;left:0;bottom:0;width:100%;height:58px;background:rgba(51,184,164,.82);color:var(--white);font-family:"Montserrat",sans-serif;font-weight:600;font-size:26px;display:flex;align-items:center;justify-content:center}

/* team */
.team{left:385px;top:3359px;width:437px;height:366px;background:
  radial-gradient(ellipse 50px 150px at 75px 230px,rgba(235,238,240,1),rgba(235,238,240,0) 80%),
  radial-gradient(ellipse 45px 140px at 165px 240px,rgba(230,233,236,1),rgba(230,233,236,0) 80%),
  radial-gradient(ellipse 55px 160px at 265px 220px,rgba(225,229,233,1),rgba(225,229,233,0) 80%),
  radial-gradient(ellipse 45px 140px at 360px 240px,rgba(232,235,238,1),rgba(232,235,238,0) 80%),
  radial-gradient(ellipse 200px 40px at 220px 350px,rgba(160,165,170,.35),rgba(160,165,170,0) 80%),
  linear-gradient(180deg,#fff,#fff)}
.team-mark{left:590px;top:3348px;width:70px;height:70px;border:4px solid var(--teal);border-radius:50%}

/* appointment form */
.appt{left:233px;top:3883px;width:728px;height:416px;border:4px solid var(--teal-soft);background:linear-gradient(180deg,#f4f7f7 0%,#dfeeec 45%,#5fb4a7 100%)}
.appt h3{position:absolute;top:26px;left:0;width:100%;text-align:center;font-family:"Montserrat",sans-serif;font-weight:500;font-size:42px;color:var(--ink)}
.appt h3 span{color:var(--teal)}
.pill{position:absolute;left:33px;width:316px;height:40px;border:2px solid var(--teal-soft);border-radius:20px;background:var(--white);font-size:12px;color:var(--muted);padding-left:42px;display:flex;align-items:center}
.appt .note{position:absolute;left:366px;top:86px;width:316px;height:164px;border:2px solid var(--teal-soft);background:var(--white);font-size:12px;color:var(--muted);padding:14px 38px}
.appt .submit{position:absolute;left:366px;top:269px;width:316px;height:42px;border-radius:21px;background:var(--teal);border:2px solid var(--white);color:var(--white);font-family:"Montserrat",sans-serif;font-weight:600;font-size:14px;display:flex;align-items:center;justify-content:center}
.appt .history{position:absolute;left:0;bottom:0;width:100%;height:62px;background:#1a2624;color:var(--white);font-family:"Montserrat",sans-serif;font-weight:600;font-size:22px;display:flex;align-items:center;justify-content:center}

/* contact */
.contact-bg{left:0;top:4389px;width:1200px;height:560px;background:
  radial-gradient(ellipse 260px 160px at 160px 250px,rgba(230,232,235,.45),rgba(230,232,235,0) 70%),
  radial-gradient(ellipse 200px 120px at 1080px 180px,rgba(220,225,228,.35),rgba(220,225,228,0) 70%),
  radial-gradient(ellipse 500px 60px at 600px 40px,rgba(200,205,210,.35),rgba(200,205,210,0) 70%),
  radial-gradient(ellipse 300px 120px at 300px 480px,rgba(170,175,180,.35),rgba(170,175,180,0) 70%),
  linear-gradient(180deg,#3f484b 0%,#555f62 50%,#2e3537 100%)}
.contact-title{left:0;width:1200px;top:4412px;text-align:center;font-family:"Montserrat",sans-serif;font-weight:600;font-size:44px;color:var(--white)}
.contact-title span{color:var(--teal)}
.contact-lede{left:295px;width:620px;top:4466px;text-align:center;font-size:14px;line-height:17px;color:var(--white)}
.c-icon{position:absolute;left:254px;width:50px;height:50px;border-radius:50%;background:var(--white);display:flex;align-items:center;justify-content:center}
.c-head{position:absolute;left:328px;font-family:"Montserrat",sans-serif;font-weight:600;font-size:22px;color:var(--teal)}
.c-text{position:absolute;left:328px;font-size:17px;line-height:19px;color:var(--white);width:330px}
.map{left:661px;top:4551px;width:323px;height:295px;border:3px solid var(--white);background:
  radial-gradient(ellipse 60px 200px at 80px 150px,rgba(90,170,200,.9),rgba(90,170,200,0) 75%),
  radial-gradient(ellipse 50px 150px at 200px 180px,rgba(95,175,205,.85),rgba(95,175,205,0) 75%),
  radial-gradient(ellipse 120px 60px at 160px 280px,rgba(95,175,205,.8),rgba(95,175,205,0) 75%),
  radial-gradient(ellipse 80px 80px at 270px 80px,rgba(240,225,160,.8),rgba(240,225,160,0) 75%),
  linear-gradient(135deg,#d4e6b8 0%,#c5deb0 50%,#dbe7c6 100%)}

/* footer */
.foot{left:0;top:4940px;width:1200px;height:365px;background:linear-gradient(180deg,#f2f8f7,#ffffff 60%)}
.foot-nav{left:0;width:1200px;top:5150px;display:flex;justify-content:center;gap:28px;font-family:"Montserrat",sans-serif;font-size:14px;color:var(--text)}
.foot-social{left:0;width:1200px;top:5218px;display:flex;justify-content:center;gap:8px}
.foot-social b{display:block;width:26px;height:26px;border-radius:50%}
.foot-contact{left:0;width:1200px;top:5265px;text-align:center;font-size:12px;color:var(--text)}
.bottom{left:0;top:5304px;width:1200px;height:53px;background:var(--ink);color:var(--white);font-size:11px}
</style>
</head>
<body>

<div class="abs topbar">Call: 123 456 7890 &nbsp;|&nbsp; info@brackwatervalemedical.com
  <div class="social"><b style="background:#3b5998"></b><b style="background:#3aa1e0"></b><b style="background:#dd4b39"></b><b style="background:#cc2222"></b></div>
</div>
<div class="abs navband">
  <nav class="nav"><span>HOME</span><span>ABOUT US</span><span>STAFF</span><span>SERVICES</span><span>BLOG</span><span>CONTACT US</span></nav>
  <div class="cta">SCHEDULE APPOINTMENT</div>
</div>
<div class="abs header-brand"><div class="brand"><i style="width:14px;height:14px;flex:none"></i>Brackwater Vale Medical</div></div>

<div class="abs hero-photo" role="img" aria-label="Bright modern clinic reception desk and glass-walled corridor"></div>
<svg class="abs" style="left:0;top:840px" width="1200" height="270" viewBox="0 0 1200 270">
  <path d="M0 240 Q420 20 1200 60 L1200 270 L0 270 Z" fill="var(--teal)"/>
  <path d="M0 262 Q420 44 1200 84 L1200 270 L0 270 Z" fill="#fff"/>
</svg>
<div class="abs hero-title">Living Health Matters</div>
<div class="abs hero-sub">Lorem ipsum dolor sit amet, consectetuer adipiscing elit, sed diam nonummy nibh.</div>
<div class="btn" style="left:133px;top:564px;width:185px;height:50px">Contact Us</div>

<div class="abs book">
  <h3>Book An Appointment</h3>
  <div class="field" style="left:25px;top:135px;width:195px">NAME</div>
  <div class="field" style="left:236px;top:135px;width:195px">PHONE</div>
  <div class="field" style="left:25px;top:189px;width:195px">EMAIL</div>
  <div class="field" style="left:236px;top:189px;width:195px">ADDRESS</div>
  <div class="field" style="left:25px;top:243px;width:406px">CONCERN<div class="drop"><svg width="40" height="34"><path d="M14 14 L26 14 L20 21 Z" fill="#fff"/></svg></div></div>
  <div class="field" style="left:25px;top:297px;width:406px;height:116px;align-items:flex-start;padding-top:16px">HOW CAN WE HELP ?</div>
  <div class="btn" style="left:191px;top:426px;width:240px;height:46px;font-size:14px;border-radius:2px">Set Appointment</div>
</div>

<div class="abs about-title">ABOUT <div class="brand"><i style="width:12px;height:12px;flex:none"></i>Brackwater Vale Medical</div></div>
<p class="abs about-copy">Lorem ipsum dolor sit amet, consectetuer adipiscing elit, sed diam nonummy nibh euismod tincidunt ut laoreet dolore magna aliquam erat volutpat. Ut wisi enim ad minim veniam, quis nostrud exerci tation ullamcorper suscipit lobortis nisl ut aliquip ex ea commodo consequat.</p>
<div class="btn" style="left:135px;top:1253px;width:188px;height:50px">Read More</div>

<div class="abs why-bg"></div>
<svg class="abs" style="left:0;top:1690px" width="1200" height="200" viewBox="0 0 1200 200">
  <path d="M0 0 L1200 0 L1200 10 Q600 20 0 190 Z" fill="#fff"/>
  <path d="M0 190 Q600 20 1200 10 L1200 60 Q600 60 0 200 Z" fill="var(--teal)" opacity=".9"/>
</svg>
<div class="section-title" style="top:1390px">OUR <span>SERVICES</span></div>
<p class="lede" style="top:1464px">Lorem ipsum dolor sit amet, consectetuer adipiscing elit, sed diam nonummy nibh euismod tincidunt ut laoreet dolore magna aliquam erat volutpat. Ut wisi enim ad minim veniam, quis nostrud exerci tation ullamcorper suscipit lobortis nisl ut aliquip ex ea commodo consequat.</p>
<div class="arrow" style="left:30px">&lsaquo;</div>
<div class="arrow" style="left:1145px">&rsaquo;</div>
<div class="svc-card" style="left:77px" role="img" aria-label="Doctor examining a patient with nurses at the bedside"></div>
<div class="svc-card" style="left:433px" role="img" aria-label="Doctor examining a patient with nurses at the bedside"></div>
<div class="svc-card" style="left:790px" role="img" aria-label="Doctor examining a patient with nurses at the bedside"></div>
<div class="svc-label" style="left:77px">OUR SERVICE 1</div>
<div class="svc-label" style="left:433px;top:1887px">OUR SERVICE 2</div>
<div class="svc-label" style="left:790px">OUR SERVICE 3</div>
<div class="btn" style="left:507px;top:1951px;width:188px;height:48px">View All</div>

<div class="section-title" style="top:2062px">WHY <span>CHOOSE US</span></div>
<p class="lede" style="top:2128px;color:#f4fbfa">Lorem ipsum dolor sit amet, consectetuer adipiscing elit, sed diam nonummy nibh euismod tincidunt ut laoreet dolore magna aliquam erat volutpat. Ut wisi enim ad minim veniam, quis nostrud exerci tation ullamcorper suscipit lobortis nisl ut aliquip ex ea commodo consequat.</p>

<div class="why-icon" style="left:266px"><svg width="64" height="64" viewBox="0 0 64 64"><circle cx="38" cy="24" r="16" fill="var(--teal)"/><path d="M26 36 L8 56" stroke="var(--teal)" stroke-width="7" stroke-linecap="round"/></svg></div>
<div class="why-icon" style="left:530px"><svg width="64" height="64" viewBox="0 0 64 64"><circle cx="32" cy="32" r="30" fill="var(--teal)"/><path d="M18 32 L28 42 L48 20" stroke="var(--ink)" stroke-width="7" fill="none" stroke-linecap="round"/></svg></div>
<div class="why-icon" style="left:788px"><svg width="64" height="64" viewBox="0 0 64 64" fill="none" stroke="var(--teal)" stroke-width="4"><circle cx="12" cy="12" r="6" fill="var(--teal)"/><circle cx="52" cy="52" r="6" fill="var(--teal)"/><path d="M18 12 H46 Q56 12 56 22 Q56 32 46 32 H18 Q8 32 8 42 Q8 52 18 52 H46"/></svg></div>

<div class="why-title" style="left:203px">PROFESSIONALISM</div>
<div class="why-title" style="left:467px">BEST RESULTS</div>
<div class="why-title" style="left:730px">SERVICE QUALITY</div>
<p class="why-copy" style="left:203px">Lorem ipsum dolor sit amet, consectetuer adipiscing elit, sed diam nonummy nibh euismod tincidunt ut laoreet</p>
<p class="why-copy" style="left:467px">Lorem ipsum dolor sit amet, consectetuer adipiscing elit, sed diam nonummy nibh euismod tincidunt ut laoreet</p>
<p class="why-copy" style="left:730px">Lorem ipsum dolor sit amet, consectetuer adipiscing elit, sed diam nonummy nibh euismod tincidunt ut laoreet</p>
<div class="mini" style="left:310px">&rsaquo;</div>
<div class="mini" style="left:570px">&rsaquo;</div>
<div class="mini" style="left:833px">&rsaquo;</div>
<div class="btn" style="left:507px;top:2583px;width:188px;height:47px">Learn More</div>

<div class="section-title" style="top:2690px">WE <span>OFFER</span></div>
<p class="lede" style="top:2756px">Lorem ipsum dolor sit amet, consectetuer adipiscing elit, sed diam nonummy nibh euismod tincidunt ut laoreet dolore magna aliquam erat volutpat. Ut wisi enim ad minim veniam, quis nostrud exerci tation ullamcorper suscipit lobortis nisl ut aliquip ex ea commodo consequat.</p>
<div class="offer" style="left:125px" role="img" aria-label="Caregiver sharing a health leaflet with a patient"><div class="cap">Education For Patients</div></div>
<div class="offer pro" style="left:611px" role="img" aria-label="Nurse standing in front of a bookshelf"><div class="cap">Education For Professionals</div></div>
<div class="btn" style="left:507px;top:3178px;width:188px;height:50px">Learn More</div>

<div class="section-title" style="top:3296px">OUR <span style="font-weight:700">TEAM</span></div>
<div class="abs team" role="img" aria-label="Four doctors in white coats standing together"></div>
<div class="abs team-mark"></div>
<div class="abs" style="left:638px;top:3530px;width:28px;height:28px;border-radius:50%;background:var(--teal);color:#fff;display:flex;align-items:center;justify-content:center;font-size:18px">&rsaquo;</div>
<div class="btn" style="left:505px;top:3748px;width:190px;height:48px;font-size:14px">See Your Doctor</div>

<div class="abs appt">
  <h3>Book <span>Appointment</span></h3>
  <div class="pill" style="top:90px">Name</div>
  <div class="pill" style="top:150px">Schedule Date</div>
  <div class="pill" style="top:210px">Phone</div>
  <div class="pill" style="top:273px">Email</div>
  <div class="note">How can we help you?</div>
  <div class="submit">SUBMIT</div>
  <div class="history">Fill Up Medical History Form &gt;&gt;</div>
</div>

<div class="abs contact-bg" role="img" aria-label="Softly lit modern clinic interior"></div>
<div class="abs contact-title">Contact <span>US</span></div>
<p class="abs contact-lede">Lorem ipsum dolor sit amet, consectetuer adipiscing elit, sed diam nonummy nibh euismod tincidunt ut laoreet dolore magna aliquam erat volutpat. Ut wisi enim ad minim veniam, quis nostrud exerci tation ullamcorper suscipit lobortis nisl ut aliquip.</p>

<div class="c-icon" style="top:4572px"><svg width="22" height="26" viewBox="0 0 22 26"><path d="M11 25 C4 16 2 12 2 9 A9 9 0 0 1 20 9 C20 12 18 16 11 25Z" fill="none" stroke="var(--teal)" stroke-width="2"/><circle cx="11" cy="9" r="3" fill="var(--teal)"/></svg></div>
<div class="c-head" style="top:4566px">Address</div>
<div class="c-text" style="top:4594px">Your Address here ....Lorem ipsum dolor sit amet, consectetuer adipiscing elit, sed diam nonummy nibh</div>

<div class="c-icon" style="top:4682px"><svg width="24" height="24" viewBox="0 0 24 24"><path d="M5 2 L9 2 L11 7 L8 9 Q10 14 15 16 L17 13 L22 15 L22 19 Q22 22 19 22 Q3 20 2 5 Q2 2 5 2Z" fill="none" stroke="var(--teal)" stroke-width="2"/></svg></div>
<div class="c-head" style="top:4676px">Give Us A Call</div>
<div class="c-text" style="top:4704px;font-weight:600">123 456 7890</div>

<div class="c-icon" style="top:4782px"><svg width="26" height="20" viewBox="0 0 26 20"><rect x="1" y="1" width="24" height="18" rx="2" fill="none" stroke="var(--teal)" stroke-width="2"/><path d="M1 3 L13 12 L25 3" fill="none" stroke="var(--teal)" stroke-width="2"/></svg></div>
<div class="c-head" style="top:4774px">Send Us A Message</div>
<div class="c-text" style="top:4802px">info@brackwatervalemedical.com</div>

<div class="abs map" role="img" aria-label="Street map showing the clinic location by the river"></div>

<div class="abs foot"></div>
<svg class="abs" style="left:0;top:4900px" width="1200" height="200" viewBox="0 0 1200 200">
  <path d="M0 40 L1200 40 L1200 110 Q700 0 0 190 Z" fill="#eaf4f2"/>
  <path d="M0 160 Q640 -10 1200 80 L1200 96 Q640 10 0 178 Z" fill="var(--teal)"/>
</svg>
<div class="abs" style="left:0;width:1200px;top:5040px;display:flex;justify-content:center">
  <div class="brand" style="font-size:30px"><i style="width:22px;height:22px"></i>Brackwater Vale Medical</div>
</div>
<nav class="abs foot-nav"><span>HOME</span><span>ABOUT US</span><span>STAFF</span><span>SERVICES</span><span>BLOG</span><span>CONTACT US</span></nav>
<div class="abs foot-social"><b style="background:#3b5998"></b><b style="background:#3aa1e0"></b><b style="background:#dd4b39"></b><b style="background:#cc2222"></b></div>
<div class="abs foot-contact">Call: &nbsp;123 456 7890 &nbsp;|&nbsp; info@brackwatervalemedical.com</div>
<div class="abs bottom">
  <span class="abs" style="left:110px;top:20px">Brackwater Vale Medical. All Rights Reserved.</span>
  <span class="abs" style="right:120px;top:20px">Our Policy &amp; Privacy and Terms Apply.</span>
</div>

</body>
</html>
```